Biz card p jester

I am a children's entertainer for birthdays, functions, events,festivals doing crazy silliness , balloon twisting ,mad magic , fantastic Facepainting and airbrush tattoos . High energy act focused on fun more than skill.
Very popular with under 5s
My makeup is a rainbow across my eyes
Want a card that kids love and pass on to parents
Like the colours magenta brite blue and yellow
Maybe 'Pipsy the jester ' in a circle
Updates
like the colours hot pink, blue and yellow
thinking "Pipsy the jester" inside a shape
Target Market(s)
Parents,event organisers,kids
Industry/Entity Type
Events
Contact Information for Business Card
Pipsy the jester
Entertainment
0417362915
Pipsythejester.com.au
Pipsythejester@fizzmail.com
Look and feel
Each slider illustrates characteristics of the customer's brand and the style your logo design should communicate.

```html
<!DOCTYPE html>
<html lang="en">
<head>
<meta charset="utf-8">
<title>Pipsy the jester – Business Card</title>
<link href="https://fonts.googleapis.com/css2?family=Cinzel:wght@400;700&family=Comfortaa:wght@400;700&display=swap" rel="stylesheet">
<style>
  :root {
    --stage: #3a2f3d;
    --card-pink: #f6a9dc;
    --card-pale: #f8d6ec;
    --edge-yellow: #f5e61c;
    --ink-purple: #7a2a8f;
    --brite-blue: #39b4ea;
    --hot-pink: #e8489a;
    --streamer-violet: #b05fc0;
    --streamer-peach: #f4a07a;
  }
  * { box-sizing: border-box; margin: 0; padding: 0; }
  html, body { width: 1200px; height: 900px; overflow: hidden; }
  body {
    background: var(--stage);
    display: flex;
    flex-direction: column;
    align-items: center;
    justify-content: center;
    gap: 40px;
    font-family: "Comfortaa", sans-serif;
  }
  .card {
    position: relative;
    width: 700px;
    height: 400px;
    border: 4px solid var(--edge-yellow);
    overflow: hidden;
  }

  /* Front */
  .card--front { background: var(--card-pale); }
  .confetti-field {
    position: absolute; inset: 0;
    background:
      radial-gradient(ellipse at 85% 30%, rgba(176,95,192,.45), transparent 55%),
      radial-gradient(ellipse at 15% 10%, rgba(232,72,154,.4), transparent 50%),
      radial-gradient(ellipse at 90% 85%, rgba(244,160,122,.4), transparent 50%),
      linear-gradient(160deg, var(--card-pale), #fbe3f2);
  }
  .brand {
    position: absolute;
    display: flex; align-items: center; gap: 14px;
  }
  .card--front .brand { top: 90px; left: 250px; }
  .brand__dot {
    width: 28px; height: 28px; border-radius: 50%;
    background: var(--brite-blue);
  }
  .brand__name {
    font-family: "Comfortaa", sans-serif;
    font-weight: 700;
    font-size: 40px;
    color: var(--ink-purple);
  }
  .tagline {
    position: absolute;
    font-weight: 700;
    color: var(--ink-purple);
  }
  .card--front .tagline { top: 150px; left: 292px; font-size: 22px; }
  .contact-list {
    position: absolute; top: 215px; left: 120px;
    list-style: none;
    display: flex; flex-direction: column; gap: 10px;
  }
  .contact-list__item {
    display: flex; align-items: center; gap: 12px;
    font-size: 20px; color: var(--ink-purple);
  }
  .contact-list__icon {
    width: 24px; height: 24px; border-radius: 50%;
    background: var(--ink-purple);
    display: flex; align-items: center; justify-content: center;
  }

  /* Back */
  .card--back { background: var(--card-pink); }
  .card--back .brand { top: 40px; left: 120px; }
  .card--back .brand__name { font-size: 30px; }
  .card--back .tagline { top: 88px; left: 162px; font-size: 16px; }
  .handprints {
    position: absolute; top: 150px; left: 80px;
    width: 130px; height: 60px; border-radius: 30px;
    background: linear-gradient(90deg, var(--brite-blue), var(--ink-purple), #7cc242, var(--brite-blue));
  }
  .services {
    position: absolute; top: 140px; left: 250px; width: 400px;
    font-family: "Cinzel", serif;
    font-size: 19px; line-height: 1.3;
    text-align: center;
    color: var(--ink-purple);
    list-style: none;
  }
</style>
</head>
<body>

  <section class="card card--front" aria-label="Business card front">
    <div class="confetti-field" role="img" aria-label="Colourful party confetti and curling streamers"></div>
    <div class="brand">
      <span class="brand__dot"></span>
      <span class="brand__name">Pipsy the jester</span>
    </div>
    <p class="tagline">Entertainment</p>
    <ul class="contact-list">
      <li class="contact-list__item">
        <span class="contact-list__icon">
          <svg width="14" height="14" viewBox="0 0 24 24"><path fill="#fff" d="M6.6 10.8a15 15 0 0 0 6.6 6.6l2.2-2.2c.3-.3.7-.4 1-.2 1.1.4 2.3.6 3.6.6.6 0 1 .4 1 1V20c0 .6-.4 1-1 1A17 17 0 0 1 3 4c0-.6.4-1 1-1h3.5c.6 0 1 .4 1 1 0 1.3.2 2.5.6 3.6.1.3 0 .7-.2 1z"/></svg>
        </span>
        0417 362 915
      </li>
      <li class="contact-list__item">
        <span class="contact-list__icon">
          <svg width="14" height="14" viewBox="0 0 24 24"><rect x="3" y="6" width="18" height="12" rx="1" fill="none" stroke="#fff" stroke-width="2"/><path d="M3 7l9 6 9-6" fill="none" stroke="#fff" stroke-width="2"/></svg>
        </span>
        Pipsythejester@fizzmail.com
      </li>
      <li class="contact-list__item">
        <span class="contact-list__icon">
          <svg width="14" height="14" viewBox="0 0 24 24"><circle cx="10" cy="10" r="6" fill="none" stroke="#fff" stroke-width="2.5"/><path d="M14.5 14.5L20 20" stroke="#fff" stroke-width="2.5"/></svg>
        </span>
        Pipsythejester.com.au
      </li>
    </ul>
  </section>

  <section class="card card--back" aria-label="Business card back">
    <div class="brand">
      <span class="brand__dot"></span>
      <span class="brand__name">Pipsy the jester</span>
    </div>
    <p class="tagline">Entertainment</p>
    <div class="handprints" role="img" aria-label="Two paint-splashed handprints in blue, purple and green"></div>
    <ul class="services">
      <li>Birthdays,</li>
      <li>Functions,</li>
      <li>Events,</li>
      <li>Festivals doing crazy silliness,</li>
      <li>Balloon twisting,</li>
      <li>Mad magic,</li>
      <li>Fantastic Facepainting and</li>
      <li>Airbrush tattoos</li>
    </ul>
  </section>

</body>
</html>
```